Computer Consulting Brochure

Computer Consulting services for schools, small businesses, local governments and medical offices. We design networks, security, monitoring, applications for these environments.
Updates
Project Deadline Extended Reason: I provided a condensed document so as not to overwhelm designers. This document covers only pertinent info that can be further condensed if necessary for physical size constraints. Added Friday, April 7, 2017
Target Market(s)
Schools, Small Businesses, Medical Offices, Local Governments. 4 brochures that are identical except for a section that specifically describes the 4 markets.
Industry/Entity Type
Computer
Colors
Designer to choose colors to be used in the design.
Look and feel
Each slider illustrates characteristics of the customer's brand and the style your logo design should communicate.

```html
<!DOCTYPE html>
<html lang="en">
<head>
<meta charset="utf-8">
<title>Veriton Systems – Trifold Brochure</title>
<link href="https://fonts.googleapis.com/css2?family=Open+Sans:wght@400;600;700&display=swap" rel="stylesheet">
<style>
  :root{
    --teal:#17a98f;
    --teal-dark:#0f8f78;
    --lime:#c6d300;
    --paper:#ffffff;
    --ink:#222222;
    --stage:#e4e4e4;
    --overlay:rgba(55,58,60,.82);
  }
  *{box-sizing:border-box;margin:0;padding:0}
  html,body{width:1200px;height:800px;overflow:hidden}
  body{background:var(--stage);font-family:"Open Sans",sans-serif;color:var(--ink)}
  .brochure{position:absolute;left:135px;top:40px;width:930px;height:720px;display:flex;box-shadow:0 10px 30px rgba(0,0,0,.18)}
  .panel{position:relative;width:310px;height:720px;background:var(--paper);overflow:hidden}
  .panel + .panel{border-left:1px solid rgba(0,0,0,.06)}
  .panel svg.shape{position:absolute;left:0;top:0;width:310px;height:720px}
  .photo{position:absolute}
  .section-title{position:absolute;left:0;width:100%;color:#fff;font-weight:700;font-size:13px;text-align:center}
  .body-copy{position:absolute;font-size:10px;line-height:1.4;text-align:justify}
  .body-copy p + p{margin-top:8px}
  .web{position:absolute;left:0;width:100%;display:flex;align-items:center;justify-content:center;gap:8px;color:#fff;font-size:15px;letter-spacing:.3px}
  .web svg{width:15px;height:15px}

  /* government panel */
  .gov .photo{left:0;top:360px;width:310px;height:330px;
    background:linear-gradient(180deg,rgba(255,255,255,1) 0%,rgba(226,230,234,.8) 35%,#c9d0d6 70%,#b7a98f 100%)}
  .gov .section-title{top:34px}
  .gov .body-copy{left:18px;right:18px;top:82px}
  .gov .web{top:688px}

  /* schools panel */
  .schools .photo{left:0;top:0;width:310px;height:640px;
    background:linear-gradient(160deg,#c9ccc0 0%,#9aa39b 30%,#6f7b84 60%,#bfc4c9 100%)}
  .schools .overlay{position:absolute;left:0;top:40px;width:310px;height:360px;background:var(--overlay)}
  .schools .section-title{top:11px}
  .schools .body-copy{left:20px;right:20px;top:54px;color:#fff;font-size:9.6px;text-align:center;line-height:1.45}
  .address{position:absolute;left:0;top:576px;width:100%;text-align:center;font-weight:700;font-size:14.5px;line-height:1.3}
  .schools .web{top:690px;font-size:14px}

  /* cover panel */
  .cover .brand{position:absolute;left:0;top:28px;width:100%;text-align:center;font-size:26px;font-weight:600;color:#333;letter-spacing:.5px}
  .cover .photo{left:0;top:98px;width:310px;height:380px;
    background:linear-gradient(120deg,#e7e2b8 0%,#d9c9b3 35%,#8a7f86 60%,#6d7fa6 80%,#3c3f55 100%)}
  .tagline{position:absolute;left:18px;right:18px;top:494px;text-align:center;font-weight:700;font-size:12.4px;line-height:1.4}
  .cover .web{top:686px}
</style>
</head>
<body>
<main class="brochure">

  <!-- Inside panel: government offices -->
  <section class="panel gov">
    <div class="photo" role="img" aria-label="Photo of a hand typing on a keyboard beside a monitor, faded into the page"></div>
    <svg class="shape" viewBox="0 0 310 720" aria-hidden="true">
      <polygon points="0,30 310,24 310,66 0,72" fill="var(--teal)"/>
      <path d="M0,680 Q155,650 310,620 L310,720 L0,720 Z" fill="var(--lime)"/>
      <path d="M0,690 Q155,662 310,634 L310,720 L0,720 Z" fill="var(--teal)"/>
    </svg>
    <h2 class="section-title">Specialized Services for Government Offices</h2>
    <div class="body-copy">
      <p>We create environments structured for government offices. We construct these environments with an object oriented approach which enables quicker implementation, simplified management and an ability to easily assimilate new technology as it becomes available. The environment supports the integration of multiple display devices, individual desktops, and secure access points to the internet.</p>
      <p>Technology is constantly changing to better serve the end user. Computing environments must be designed with this fact in mind so they may always be easily tuned and upgraded. It used to be that new technology could not be immediately incorporated because it was a massive task to incorporate new approaches. Therefore, advantages were not capitalized on when available because the changes had to accumulate in order to justify the major expense involved. That is no longer acceptable to constrained budgets and the demand for quick improvements to the office environment. That is another reason we use the object oriented approach when creating our medical office environments. It is very easy to add enhanced technology without a major restructuring of the existing environment. We install environments for all sizes and capacities; a single doctor, an integrated office with medical teams, or geographically distributed offices. We create a design for your environment using the most appropriate combination of Ethernet, wireless and fiber networks. We provide training for staff to implement applications delivered via desktops, handhelds or tablets. We install and support robust wireless systems that provide the latest security and enable specific selection criteria for each member of the staff as dictated by their needs and requirements.</p>
    </div>
    <div class="web">
      <svg viewBox="0 0 16 16" fill="none" stroke="#fff" stroke-width="1.3"><circle cx="8" cy="8" r="6.5"/><ellipse cx="8" cy="8" rx="3" ry="6.5"/><line x1="1.5" y1="8" x2="14.5" y2="8"/></svg>
      www.veritonsystems.com
    </div>
  </section>

  <!-- Inside panel: schools -->
  <section class="panel schools">
    <div class="photo" role="img" aria-label="Photo of a computer lab with monitors and keyboards"></div>
    <div class="overlay"></div>
    <svg class="shape" viewBox="0 0 310 720" aria-hidden="true">
      <rect x="0" y="0" width="310" height="40" fill="var(--teal)"/>
      <path d="M0,590 Q155,550 310,515 L310,720 L0,720 Z" fill="var(--lime)"/>
      <path d="M0,600 Q155,562 310,529 L310,720 L0,720 Z" fill="#f4f4f4"/>
      <path d="M0,672 Q155,664 310,650 L310,720 L0,720 Z" fill="var(--lime)"/>
      <path d="M0,680 Q155,674 310,662 L310,720 L0,720 Z" fill="var(--teal)"/>
    </svg>
    <h2 class="section-title">Specialized Services for Schools</h2>
    <div class="body-copy">
      <p>We create environments structured for educational objectives. These educational specific environments are tailored to the learning process. We construct these environments with an object oriented approach which enables quicker implementation, simplified management and an ability to easily assimilate new technology as it becomes available. The environment is enhanced to easily integrate student monitoring by either human or automated interfaces. The environment supports the integration of multiple display devices, desktop virtualization if cost effective, and controlled access to the internet enabling easy access to seminars and selected lectures by notable gifted instructors.</p>
      <p>We cater to all sizes and capacities; either school, campus or district. We will create a design for your network using the most appropriate combination of Ethernet, wireless and fiber networks. We provide training for teachers to implement leading edge educational applications delivered via desktops, handhelds or tablets. We install and support robust, secure wireless systems enabling selection criteria for each student that can filter or block internet activity by any combination of user, device, day, time of day and type of application.</p>
    </div>
    <div class="address">18 Harbor Rd #210,<br>Millbrook, RI 02800-0210<br>Tel: 401-555-0142</div>
    <div class="web">
      <svg viewBox="0 0 16 16" fill="none" stroke="#fff" stroke-width="1.3"><circle cx="8" cy="8" r="6.5"/><ellipse cx="8" cy="8" rx="3" ry="6.5"/><line x1="1.5" y1="8" x2="14.5" y2="8"/></svg>
      info@VeritonSystems.com
    </div>
  </section>

  <!-- Front cover -->
  <section class="panel cover">
    <div class="photo" role="img" aria-label="Photo of students working at computers in a classroom"></div>
    <svg class="shape" viewBox="0 0 310 720" aria-hidden="true">
      <path d="M0,0 L310,0 L310,70 Q155,104 0,84 Z" fill="#fff"/>
      <path d="M0,84 Q155,104 310,70 L310,84 Q155,118 0,98 Z" fill="var(--teal)"/>
      <path d="M0,490 Q155,430 310,440 L310,720 L0,720 Z" fill="var(--lime)"/>
      <path d="M0,504 Q155,448 310,456 L310,720 L0,720 Z" fill="#f6f6f6"/>
      <path d="M0,666 Q155,658 310,636 L310,720 L0,720 Z" fill="var(--lime)"/>
      <path d="M0,676 Q155,670 310,650 L310,720 L0,720 Z" fill="var(--teal)"/>
    </svg>
    <h1 class="brand">Veriton Systems</h1>
    <p class="tagline">PROVIDING DESIGN,<br>INSTALLATION and MANAGEMENT<br>of Computing Environments that<br>are enhanced for Schools,<br>Small Businesses and Local Governments<br>Security Camera Monitoring Systems<br>that are integrated into<br>the Computing Environment</p>
    <div class="web">
      <svg viewBox="0 0 16 16" fill="none" stroke="#fff" stroke-width="1.3"><circle cx="8" cy="8" r="6.5"/><ellipse cx="8" cy="8" rx="3" ry="6.5"/><line x1="1.5" y1="8" x2="14.5" y2="8"/></svg>
      www.veritonsystems.com
    </div>
  </section>

</main>
</body>
</html>
```